KerrLow Farm

Need a nice simple clean double sided business card that has our logo and info on:
Kerr Low Farm
Martin & Felicity Kerr Low
kerrlowfarm@mailbarn.example
Martin: 1-780-555-0148
Felicity: 1-780-555-0193
Instagram @ kerrlow_farm

Contact Information for Business Card

Martin & Felicity Kerr Low kerrlowfarm@mailbarn.example Martin: 1-780-555-0148 Felicity: 1-780-555-0193

```html
<!DOCTYPE html>
<html lang="en">
<head>
<meta charset="utf-8">
<title>Kerr Low Farm — Business Card</title>
<link rel="stylesheet" href="https://fonts.googleapis.com/css2?family=Mulish:wght@400;600;700&display=swap">
<style>
  :root {
    --page-bg: #f9f9f9;
    --card-white: #ffffff;
    --farm-green: #5b9a1d;
    --leaf-green: #67a00f;
    --harvest-orange: #f39a1b;
    --ink-white: #ffffff;
  }
  * { margin: 0; padding: 0; box-sizing: border-box; }
  html, body {
    width: 1200px; height: 800px; overflow: hidden;
    background: var(--page-bg);
    font-family: "Mulish", "Helvetica Neue", Arial, sans-serif;
  }
  .stage { position: relative; width: 1200px; height: 800px; }

  .card {
    position: absolute; left: 318px; width: 564px; height: 322px;
    box-shadow: 0 1px 3px rgba(0,0,0,0.12);
  }
  .card--front { top: 64px; background: var(--card-white); }
  .card--back { top: 413px; background: var(--leaf-green); }

  /* Front */
  .owners {
    position: absolute; left: 25px; top: 86px;
    font-size: 17px; font-weight: 400; letter-spacing: 1.2px;
    color: var(--farm-green); text-transform: uppercase; white-space: nowrap;
  }
  .farm-title {
    position: absolute; left: 25px; top: 110px;
    font-size: 15px; font-weight: 400; letter-spacing: 0.3px;
    color: var(--harvest-orange); text-transform: uppercase;
  }
  .brand-seal {
    position: absolute; left: 380px; top: 37px; width: 126px; height: 126px;
    border: 3.5px solid var(--farm-green); border-radius: 50%;
    display: flex; align-items: center; justify-content: center; text-align: center;
    font-size: 15px; font-weight: 700; line-height: 1.2; color: var(--farm-green);
  }
  .contact-row {
    position: absolute; left: 25px;
    font-size: 17px; color: var(--farm-green); white-space: nowrap;
  }
  .contact-row strong { font-weight: 700; }
  .contact-row .sep { margin: 0 10px; font-size: 14px; }
  .contact-row--phones { top: 226px; }
  .contact-row--online { top: 270px; font-size: 16.5px; }
  .divider {
    position: absolute; left: 25px; top: 256px; width: 501px; height: 2px;
    background: var(--harvest-orange);
  }

  /* Back */
  .back-seal {
    position: absolute; left: 229px; top: 83px; width: 106px; height: 106px;
    border: 3.5px solid var(--ink-white); border-radius: 50%;
  }
  .back-name {
    position: absolute; left: 0; right: 0; top: 193px; text-align: center;
    font-size: 30px; font-weight: 600; letter-spacing: 0.5px;
    color: var(--ink-white); text-transform: uppercase;
  }
  .back-tagline {
    position: absolute; left: 0; right: 0; top: 229px; text-align: center;
    font-size: 13px; font-weight: 400; letter-spacing: 8.5px; padding-left: 8px;
    color: var(--ink-white); text-transform: uppercase;
  }
</style>
</head>
<body>
<main class="stage">
  <section class="card card--front" aria-label="Business card front">
    <p class="owners">Martin &amp; Felicity Kerr Low</p>
    <p class="farm-title">Kerr Low Farm</p>
    <div class="brand-seal">Kerr Low<br>Farm</div>
    <p class="contact-row contact-row--phones">
      <strong>Martin:</strong>&nbsp; 1-780-555-0148<span class="sep">|</span><strong>Felicity:</strong>&nbsp; 1-780-555-0193
    </p>
    <div class="divider"></div>
    <p class="contact-row contact-row--online">
      <strong>E:</strong>&nbsp; kerrlowfarm@mailbarn.example<span class="sep">|</span><strong>Instagram</strong> @ kerrlow_farm
    </p>
  </section>

  <section class="card card--back" aria-label="Business card back">
    <div class="back-seal"></div>
    <p class="back-name">Kerr Low Farm</p>
    <p class="back-tagline">Stone Milled Flour</p>
  </section>
</main>
</body>
</html>
```